Tidewell Private Yacht Charter "Rack Flyer"

This will be a 4" x 9" Rack flyer that is 4 colors and two sided. This is a Private Yacht charter company that is based in St Thomas, U.S. Virgin Islands. Our main product that I would like to promote on one entire side of the flyer is our Private Luxury Full Day "Glimmer Feast". our charter company is unique in the fact we offer customizable itineraries and we offer unique activities that keep the family and groups engaged in fun for the entire day. We would like something with our colors.

Target Market(s)

We are trying to reach an upscale clients that are looking for a Luxury Day Charter experience. these people will be most likely staying in Private Villas or staying at the Halvern Crest or QP Delacourt.

Requirements
Must have
• Contact Information:
Ph: (340) 555-0187
email: Info@tidewellvi.example
www.tidewellvi.example
One side should Promote our Glimmer Feast (Glimmer Feast is a trademarked name).
All Guests will receive "Welcome Mimosas"
> Up to 12 guests
> Full Brunch Spread to include, Assorted fruit tower, Artesian Waffle Board, Frittata's, Loaded Avocado Toast or an All American Breakfast.
> Specialty Cocktails with Bottle Service options available
List all of our Unique activities to include:
Snorkeling
Underwater WaveGlider
Cliff Diving
Paddleboarding
Towable Activities
TEXT TO BE WRITTEN:
Experience yacht charter service at its Finest!
Sail away with us on a Luxury Charter experience complete with a full brunch spread. During our sail we will take you to the hottest destination spots in the Caribbean surrounding St Thomas and St John. Warm, fresh baked afternoon cookies will be served on the way back from our days journeys. Unlimited water, sodas, beer and rum punch will be provided for the entire group to enjoy throughout the day.
_________________

On side two of the brochure you can refer to the downloaded text. We do not want pricing listed on the flyer

```html
<!DOCTYPE html>
<html lang="en">
<head>
<meta charset="utf-8">
<title>Tidewell Charters – Rack Flyer</title>
<link href="https://fonts.googleapis.com/css2?family=Montserrat:wght@400;500;600&family=Oswald:wght@700&display=swap" rel="stylesheet">
<style>
  :root{
    --bg:#5c5c5c;
    --navy:#1b4ea0;
    --red:#e3202c;
    --ink:#2e2e2e;
    --paper:#ffffff;
  }
  html,body{margin:0;padding:0;width:1200px;height:1200px;overflow:hidden;background:var(--bg);}
  body{position:relative;font-family:"Montserrat",sans-serif;color:var(--ink);}
  .flyer{position:absolute;top:167px;width:378px;height:850px;background:var(--paper);overflow:hidden;}
  .flyer--front{left:142px;}
  .flyer--back{left:619px;}
  .photo{position:absolute;left:0;width:378px;}
  .photo--bay{top:0;height:420px;background:linear-gradient(180deg,#8fc4ef 0%,#cfe6f7 18%,#3f8f5a 26%,#2fc2d8 38%,#1aa7c9 55%,#3b8a3a 75%,#2f6d2a 100%);}
  .photo--guests{top:0;height:300px;background:linear-gradient(135deg,#f3ede6 0%,#d7b99a 40%,#b47c4e 70%,#e9e4de 100%);}
  .photo--lookout{top:540px;height:240px;background:linear-gradient(180deg,#eef4fa 0%,#bcd8ee 25%,#2f7fc0 50%,#6d8f5a 75%,#c9d8e6 100%);}
  .shapes{position:absolute;inset:0;}
  .brand{position:absolute;left:0;width:378px;top:452px;text-align:center;}
  .brand__name{font-weight:600;font-size:38px;color:var(--red);letter-spacing:.5px;line-height:1;}
  .brand__mark{display:inline-block;width:12px;height:12px;border-radius:50%;background:var(--red);margin-left:8px;vertical-align:middle;}
  .brand__sub{font-weight:600;font-size:38px;color:var(--red);}
  .headline{position:absolute;top:530px;left:0;width:378px;text-align:center;font-family:"Oswald",sans-serif;font-weight:700;font-size:42px;letter-spacing:-.5px;line-height:1;margin:0;}
  .headline__red{color:var(--red);}
  .headline__blue{color:var(--navy);}
  .perks{position:absolute;top:590px;left:26px;width:326px;margin:0;padding:0;list-style:none;font-size:13.4px;line-height:16.5px;}
  .perks li{position:relative;padding-left:16px;margin-bottom:10px;text-align:justify;}
  .tick{position:absolute;left:0;top:3px;width:9px;height:9px;}
  .contact{position:absolute;left:0;width:378px;top:790px;color:#fff;font-size:11.8px;font-weight:500;text-align:center;}
  .contact__row{display:flex;justify-content:center;gap:16px;margin-bottom:9px;}
  .contact__item{display:flex;align-items:center;gap:4px;}
  .contact__item svg{width:15px;height:15px;}
  .activities{position:absolute;top:306px;left:23px;width:340px;}
  .activities__title{margin:0 0 8px;font-size:13.4px;font-weight:600;color:#222;}
  .activities__list{margin:0;padding:0;list-style:none;display:grid;grid-template-columns:160px 1fr;row-gap:3px;font-size:13px;}
  .activities__list li{position:relative;padding-left:14px;}
  .activities__list .tick{top:4px;}
  .story{position:absolute;top:396px;left:25px;width:330px;margin:0;font-size:11.9px;line-height:15px;text-align:justify;color:#333;}
</style>
</head>
<body>
  <!-- Front: Welcome Mimosas -->
  <section class="flyer flyer--front">
    <div class="photo photo--bay" role="img" aria-label="Aerial view of a turquoise Caribbean bay with green hills, small islands and a white sand beach"></div>
    <svg class="shapes" viewBox="0 0 378 850" aria-hidden="true">
      <path d="M0 410 Q150 360 378 395 L378 850 L0 850 Z" fill="#fff"/>
      <path d="M40 395 Q200 350 370 395" fill="none" stroke="var(--navy)" stroke-width="5"/>
      <path d="M70 408 Q120 400 160 412" fill="none" stroke="var(--navy)" stroke-width="2.5"/>
      <path d="M0 790 Q190 740 378 755 L378 850 L0 850 Z" fill="var(--navy)"/>
      <path d="M25 765 Q180 720 330 770" fill="none" stroke="var(--red)" stroke-width="5"/>
      <path d="M225 752 Q270 760 310 758" fill="none" stroke="var(--red)" stroke-width="2.5"/>
    </svg>
    <div class="brand">
      <div class="brand__name">Tidewell<span class="brand__mark"></span></div>
    </div>
    <h1 class="headline"><span class="headline__red">WELCOME</span> <span class="headline__blue">MIMOSAS</span></h1>
    <ul class="perks">
      <li><svg class="tick" viewBox="0 0 10 10"><circle cx="5" cy="5" r="5" fill="var(--red)"/><path d="M2.8 5.2l1.5 1.5 3-3" stroke="#fff" stroke-width="1.4" fill="none"/></svg>Up to 12 guests</li>
      <li><svg class="tick" viewBox="0 0 10 10"><circle cx="5" cy="5" r="5" fill="var(--red)"/><path d="M2.8 5.2l1.5 1.5 3-3" stroke="#fff" stroke-width="1.4" fill="none"/></svg>Full Brunch Spread to include, Assorted fruit tower, Artesian Waffle Board, Frittata's, Loaded Avocado Toast or an All American Breakfast.</li>
      <li><svg class="tick" viewBox="0 0 10 10"><circle cx="5" cy="5" r="5" fill="var(--red)"/><path d="M2.8 5.2l1.5 1.5 3-3" stroke="#fff" stroke-width="1.4" fill="none"/></svg>Specialty Cocktails with Bottle Service options available</li>
    </ul>
    <div class="contact">
      <div class="contact__row">
        <span class="contact__item"><svg viewBox="0 0 16 16"><circle cx="8" cy="8" r="7" fill="none" stroke="#fff"/><path d="M5.5 4.5l1.5 0 .7 2-1 .8a5 5 0 0 0 2 2l.8-1 2 .7 0 1.5c-4 .3-6.3-2-6-6z" fill="#fff"/></svg>(340) 555-0187</span>
        <span class="contact__item"><svg viewBox="0 0 16 16"><circle cx="8" cy="8" r="7" fill="none" stroke="#fff"/><rect x="4.5" y="5.5" width="7" height="5" fill="none" stroke="#fff"/><path d="M4.5 5.5l3.5 3 3.5-3" fill="none" stroke="#fff"/></svg>Info@tidewellvi.example</span>
      </div>
      <div class="contact__row">
        <span class="contact__item"><svg viewBox="0 0 16 16"><circle cx="8" cy="8" r="7" fill="none" stroke="#fff"/><circle cx="8" cy="8" r="4" fill="none" stroke="#fff"/><path d="M4 8h8M8 4v8" stroke="#fff"/></svg>www.tidewellvi.example</span>
      </div>
    </div>
  </section>

  <!-- Back: Activities & story -->
  <section class="flyer flyer--back">
    <div class="photo photo--guests" role="img" aria-label="Group of friends toasting with cocktails around a brunch table on a yacht deck"></div>
    <div class="photo photo--lookout" role="img" aria-label="Two girls with raised arms overlooking a blue harbour full of sailboats"></div>
    <svg class="shapes" viewBox="0 0 378 850" aria-hidden="true">
      <path d="M0 300 Q190 240 378 270 L378 0 L0 0 Z" fill="none"/>
      <path d="M0 290 Q200 330 378 260 L378 560 Q200 510 0 540 Z" fill="#fff"/>
      <path d="M20 268 Q200 315 360 270" fill="none" stroke="var(--navy)" stroke-width="5"/>
      <path d="M70 282 Q120 276 170 286" fill="none" stroke="var(--navy)" stroke-width="2.5"/>
      <path d="M0 790 Q190 740 378 755 L378 850 L0 850 Z" fill="var(--navy)"/>
      <path d="M25 765 Q180 720 330 770" fill="none" stroke="var(--red)" stroke-width="5"/>
    </svg>
    <div class="activities">
      <p class="activities__title">List all of our Unique activities to include:</p>
      <ul class="activities__list">
        <li><svg class="tick" viewBox="0 0 10 10"><circle cx="5" cy="5" r="5" fill="var(--red)"/><path d="M2.8 5.2l1.5 1.5 3-3" stroke="#fff" stroke-width="1.4" fill="none"/></svg>Snorkeling</li>
        <li><svg class="tick" viewBox="0 0 10 10"><circle cx="5" cy="5" r="5" fill="var(--red)"/><path d="M2.8 5.2l1.5 1.5 3-3" stroke="#fff" stroke-width="1.4" fill="none"/></svg>Underwater WaveGlider</li>
        <li><svg class="tick" viewBox="0 0 10 10"><circle cx="5" cy="5" r="5" fill="var(--red)"/><path d="M2.8 5.2l1.5 1.5 3-3" stroke="#fff" stroke-width="1.4" fill="none"/></svg>Cliff Diving</li>
        <li><svg class="tick" viewBox="0 0 10 10"><circle cx="5" cy="5" r="5" fill="var(--red)"/><path d="M2.8 5.2l1.5 1.5 3-3" stroke="#fff" stroke-width="1.4" fill="none"/></svg>Towable Activities</li>
        <li><svg class="tick" viewBox="0 0 10 10"><circle cx="5" cy="5" r="5" fill="var(--red)"/><path d="M2.8 5.2l1.5 1.5 3-3" stroke="#fff" stroke-width="1.4" fill="none"/></svg>Paddleboarding</li>
      </ul>
    </div>
    <p class="story">Experience yacht charter service at its Finest!<br>Sail away with us on a Luxury Charter experience complete with a full brunch spread. During our sail we will take you to the hottest destination spots in the Caribbean surrounding St Thomas and St John. Warm, fresh baked afternoon cookies will be served on the way back from our days journeys. Unlimited water, sodas, beer and rum punch will be provided for the entire group to enjoy throughout the day.</p>
    <div class="contact">
      <div class="contact__row">
        <span class="contact__item"><svg viewBox="0 0 16 16"><circle cx="8" cy="8" r="7" fill="none" stroke="#fff"/><path d="M5.5 4.5l1.5 0 .7 2-1 .8a5 5 0 0 0 2 2l.8-1 2 .7 0 1.5c-4 .3-6.3-2-6-6z" fill="#fff"/></svg>(340) 555-0187</span>
        <span class="contact__item"><svg viewBox="0 0 16 16"><circle cx="8" cy="8" r="7" fill="none" stroke="#fff"/><rect x="4.5" y="5.5" width="7" height="5" fill="none" stroke="#fff"/><path d="M4.5 5.5l3.5 3 3.5-3" fill="none" stroke="#fff"/></svg>Info@tidewellvi.example</span>
      </div>
      <div class="contact__row">
        <span class="contact__item"><svg viewBox="0 0 16 16"><circle cx="8" cy="8" r="7" fill="none" stroke="#fff"/><circle cx="8" cy="8" r="4" fill="none" stroke="#fff"/><path d="M4 8h8M8 4v8" stroke="#fff"/></svg>www.tidewellvi.example</span>
      </div>
    </div>
  </section>
</body>
</html>
```